Health and Wellness company needs flyer to promote free seminar

Stride reform studio is a health and wellness company that offers an exercise program designed by physical therapists to help relieve pain and improve mobility. Our business is a new concept that is not well understood by the public. In order to promote our business we offer a free seminar where we present information regarding the underlying cause of pain and tightness. During the seminar we also perform a posture screen and movement testing for all participants.

Target Market(s)

Mostly healthy and active women ages 25-65

Industry/Entity Type

Health And Wellness

Font styles to use
Sans Serif

Colors

Designer to choose colors to be used in the design.

Requirements
Must have
• Title: Eliminate Pain and Tightness For Good
• Paragraph: Stride Reform Studio offers a free 60 minute seminar: "The Busy Walker's Handbook to Bending and Standing Taller."
• What to Expect:
• • Identify the underlying cause of your pain and mobility issues
• • Expose what gets in the way of you moving and feeling better
• • Learn why traditional exercises don’t help and can actually make the problem worse
• • Reveal what your posture is saying and how that impacts you
• • Experience your muscle imbalances through movement tests
• • Discover the training method that realigns your posture, increases your mobility and reduces your pain
• Call to action: RSVP online at stridereformstudio.com
Nice to have
• Use a relevant image showing a female dealing with tightness in the low back, legs, etc.
• Emphasize that the seminar is FREE.
• Make the call to action prominent.

```html
<!DOCTYPE html>
<html lang="en">
<head>
<meta charset="utf-8">
<title>Stride Reform Studio – Free Seminar Flyer</title>
<link rel="stylesheet" href="https://fonts.googleapis.com/css2?family=Bebas+Neue&family=Roboto+Slab:wght@400;700&display=swap">
<style>
  :root {
    --ink-black: #000000;
    --paper-white: #ffffff;
    --title-grey: #a9abae;
    --accent-orange: #f7941d;
    --brand-purple: #5a5ea6;
    --brand-purple-deep: #4f5399;
    --body-ink: #231f20;
    --photo-light: #8a8a8a;
    --photo-dark: #1c1c1c;
  }
  html, body {
    margin: 0;
    padding: 0;
    overflow: hidden;
    background: var(--paper-white);
  }
  .flyer {
    position: relative;
    width: 927px;
    height: 1200px;
    overflow: hidden;
    background: var(--paper-white);
    font-family: "Roboto Slab", Georgia, serif;
  }
  .flyer-shapes {
    position: absolute;
    inset: 0;
  }
  .headline {
    position: absolute;
    left: 58px;
    top: 46px;
    margin: 0;
    font-family: "Bebas Neue", "Arial Narrow", sans-serif;
    font-weight: 400;
    font-size: 132px;
    line-height: 120px;
    color: var(--title-grey);
    letter-spacing: 0.5px;
  }
  .offer {
    position: absolute;
    left: 478px;
    top: 532px;
    width: 449px;
    text-align: center;
    color: var(--paper-white);
  }
  .offer-lead {
    margin: 0;
    font-weight: 700;
    font-size: 27px;
    line-height: 38px;
  }
  .offer-title {
    margin: 8px 0 0;
    font-weight: 400;
    font-size: 23px;
    line-height: 33px;
  }
  .expect-list {
    position: absolute;
    left: 34px;
    top: 690px;
    margin: 0;
    padding: 0;
    list-style: none;
    color: var(--body-ink);
    font-size: 21px;
    line-height: 33px;
  }
  .expect-item {
    position: relative;
    padding-left: 26px;
    margin-bottom: 3px;
  }
  .expect-item svg {
    position: absolute;
    left: 0;
    top: 8px;
    width: 18px;
    height: 18px;
  }
  .expect-item strong {
    font-weight: 700;
    text-decoration: underline;
    text-decoration-thickness: 1.5px;
    text-underline-offset: 6px;
  }
  .cta {
    position: absolute;
    left: 40px;
    top: 1100px;
    width: 540px;
    text-align: center;
  }
  .cta-label {
    margin: 0;
    font-weight: 700;
    font-size: 31px;
    line-height: 40px;
    color: var(--paper-white);
  }
  .cta-url {
    margin: 0;
    font-weight: 400;
    font-size: 27px;
    line-height: 40px;
    color: var(--accent-orange);
  }
  .brand {
    position: absolute;
    left: 616px;
    top: 1062px;
    width: 290px;
    text-align: center;
  }
  .brand-mark {
    display: block;
    width: 58px;
    height: 58px;
    margin: 0 auto 14px;
    background: var(--brand-purple);
  }
  .brand-name {
    margin: 0;
    font-weight: 700;
    font-size: 25px;
    line-height: 30px;
    color: var(--brand-purple);
  }
</style>
</head>
<body>
<main class="flyer">
  <svg class="flyer-shapes" width="927" height="1200" viewBox="0 0 927 1200" aria-hidden="true">
    <defs>
      <linearGradient id="photoTone" x1="0" y1="0" x2="1" y2="1">
        <stop offset="0" stop-color="var(--photo-dark)"/>
        <stop offset="0.45" stop-color="var(--photo-light)"/>
        <stop offset="1" stop-color="var(--photo-dark)"/>
      </linearGradient>
      <linearGradient id="bandTone" x1="0" y1="0" x2="1" y2="1">
        <stop offset="0" stop-color="var(--brand-purple)"/>
        <stop offset="1" stop-color="var(--brand-purple-deep)"/>
      </linearGradient>
    </defs>
    <rect class="dark-field" x="0" y="0" width="927" height="860" fill="var(--ink-black)"/>
    <polygon class="light-field" points="0,520 927,848 927,1200 0,1200" fill="var(--paper-white)"/>
    <polygon class="cta-band" points="0,1116 496,1052 632,1200 0,1200" fill="var(--ink-black)"/>
    <polygon class="offer-band" points="478,518 927,518 927,848 430,672" fill="url(#bandTone)"/>
    <path class="title-bracket" d="M35 104 V34 H104" fill="none" stroke="var(--accent-orange)" stroke-width="4"/>
    <path class="title-bracket" d="M400 530 H470 V462" fill="none" stroke="var(--accent-orange)" stroke-width="4"/>
  </svg>

  <svg class="hero-photo" role="img" aria-label="Photo of an athletic woman seen from behind in a sports top, holding her lower back" style="position:absolute;left:470px;top:0" width="457" height="518" viewBox="0 0 457 518">
    <rect width="457" height="518" fill="url(#photoTone)"/>
  </svg>

  <h1 class="headline">Eliminate<br>Pain and<br>Tightness<br>For Good</h1>

  <section class="offer">
    <p class="offer-lead">Stride Reform Studio Offers<br>a Free 60-minute Seminar:</p>
    <p class="offer-title">"The Busy Walker's Handbook to<br>Bending and Standing Taller."</p>
  </section>

  <ul class="expect-list">
    <li class="expect-item"><svg viewBox="0 0 18 18" aria-hidden="true"><circle cx="9" cy="9" r="7.5" fill="none" stroke="var(--brand-purple)" stroke-width="1.5"/><path d="M5 9l3 3 7-8" fill="none" stroke="var(--brand-purple)" stroke-width="1.6"/></svg><strong>Identify</strong> the underlying cause of your<br>pain and mobility issues</li>
    <li class="expect-item"><svg viewBox="0 0 18 18" aria-hidden="true"><circle cx="9" cy="9" r="7.5" fill="none" stroke="var(--brand-purple)" stroke-width="1.5"/><path d="M5 9l3 3 7-8" fill="none" stroke="var(--brand-purple)" stroke-width="1.6"/></svg><strong>Expose</strong> what gets in the way of you moving and<br>feeling better</li>
    <li class="expect-item"><svg viewBox="0 0 18 18" aria-hidden="true"><circle cx="9" cy="9" r="7.5" fill="none" stroke="var(--brand-purple)" stroke-width="1.5"/><path d="M5 9l3 3 7-8" fill="none" stroke="var(--brand-purple)" stroke-width="1.6"/></svg><strong>Learn</strong> why traditional exercises don’t help and can actually make<br>the problem worse</li>
    <li class="expect-item"><svg viewBox="0 0 18 18" aria-hidden="true"><circle cx="9" cy="9" r="7.5" fill="none" stroke="var(--brand-purple)" stroke-width="1.5"/><path d="M5 9l3 3 7-8" fill="none" stroke="var(--brand-purple)" stroke-width="1.6"/></svg><strong>Reveal</strong> what your posture is saying and how that impacts you</li>
    <li class="expect-item"><svg viewBox="0 0 18 18" aria-hidden="true"><circle cx="9" cy="9" r="7.5" fill="none" stroke="var(--brand-purple)" stroke-width="1.5"/><path d="M5 9l3 3 7-8" fill="none" stroke="var(--brand-purple)" stroke-width="1.6"/></svg><strong>Experience</strong> your muscle imbalances through movement tests</li>
    <li class="expect-item"><svg viewBox="0 0 18 18" aria-hidden="true"><circle cx="9" cy="9" r="7.5" fill="none" stroke="var(--brand-purple)" stroke-width="1.5"/><path d="M5 9l3 3 7-8" fill="none" stroke="var(--brand-purple)" stroke-width="1.6"/></svg><strong>Discover</strong> the training method that realigns your posture, increases your<br>mobility and reduces your pain</li>
  </ul>

  <section class="cta">
    <p class="cta-label">RSVP Online at</p>
    <p class="cta-url">stridereformstudio.com/free-seminar</p>
  </section>

  <div class="brand">
    <span class="brand-mark" aria-hidden="true"></span>
    <p class="brand-name">Stride Reform Studio</p>
  </div>
</main>
</body>
</html>
```